Brisbane IT support business needs our first facebook page

Hi All,

We are after a new facebook page for our IT solutions and support business.The business name is Marlowe Computer Network Helpdesk, or MCNH for short. We provide a range of solutions and services within the IT space.

I would like to utilize the two colours in our business logo I have uploaded.

```html
<!DOCTYPE html>
<html lang="en">
<head>
<meta charset="utf-8">
<title>Marlowe Computer Network Helpdesk – Facebook Cover</title>
<link href="https://fonts.googleapis.com/css2?family=Arimo:wght@400;700&display=swap" rel="stylesheet">
<style>
  :root {
    --orange: #f07f22;
    --teal: #1d4e5f;
    --navy: #1b3350;
    --white: #ffffff;
    --frame: #1a1a1a;
    --photo-dark: #0e2a4a;
    --photo-mid: #1f5f93;
    --photo-light: #cfe1ef;
  }
  html, body {
    margin: 0;
    padding: 0;
    overflow: hidden;
    background: var(--white);
  }
  .cover {
    position: relative;
    width: 1200px;
    height: 443px;
    overflow: hidden;
    background: var(--white);
    font-family: "Arimo", Arial, sans-serif;
  }
  .hero-art {
    position: absolute;
    inset: 0;
  }
  .brand-title {
    position: absolute;
    left: 20px;
    top: 10px;
    width: 580px;
    margin: 0;
    text-align: center;
    color: var(--orange);
    font-weight: 700;
    font-size: 28px;
    line-height: 35px;
  }
  .tagline {
    position: absolute;
    left: 70px;
    top: 119px;
    margin: 0;
    color: var(--teal);
    font-weight: 400;
    font-size: 38px;
    letter-spacing: -0.2px;
  }
  .subline {
    position: absolute;
    left: 183px;
    top: 174px;
    margin: 0;
    color: var(--orange);
    font-size: 26px;
  }
  .services {
    list-style: none;
    margin: 0;
    padding: 0;
    color: var(--navy);
    font-size: 27px;
    line-height: 27px;
  }
  .services li {
    position: absolute;
    left: 332px;
  }
  .services .svc-selection { top: 229px; }
  .services .svc-consultancy { top: 308px; left: 326px; }
  .services .svc-support { top: 374px; left: 328px; }
  .logo-box {
    position: absolute;
    left: 35px;
    top: 277px;
    width: 229px;
    height: 172px;
    border: 4px solid var(--frame);
    background: var(--white);
    display: flex;
    align-items: center;
    justify-content: center;
  }
  .logo-name {
    color: var(--teal);
    font-weight: 400;
    font-size: 36px;
    letter-spacing: 2px;
  }
</style>
</head>
<body>
  <div class="cover">
    <svg class="hero-art" width="1200" height="443" viewBox="0 0 1200 443">
      <defs>
        <linearGradient id="photoTone" x1="0" y1="0" x2="1" y2="0.4">
          <stop offset="0" stop-color="var(--photo-light)"/>
          <stop offset="0.35" stop-color="var(--photo-mid)"/>
          <stop offset="1" stop-color="var(--photo-dark)"/>
        </linearGradient>
      </defs>
      <polygon role="img" aria-label="Photo of a businessman in a suit writing the word Solution on a glass board with business strategy words"
               points="612,0 708,219 652,443 1200,443 1200,0" fill="url(#photoTone)"/>
      <polyline class="edge-stripe" points="612,0 708,219 652,443" fill="none" stroke="var(--orange)" stroke-width="9"/>
      <g class="chevrons" fill="none" stroke="var(--orange)" stroke-width="9" stroke-linejoin="miter">
        <polyline points="654,201 638,217 654,233"/>
        <polyline points="680,201 664,217 680,233"/>
      </g>
    </svg>

    <h1 class="brand-title">Marlowe Computer Network<br>Helpdesk</h1>
    <h2 class="tagline">Better at IT-Better at Business</h2>
    <p class="subline">Improve your business</p>

    <ul class="services">
      <li class="svc-selection">Solution Selection and<br>Acquisition</li>
      <li class="svc-consultancy">Consultantsy</li>
      <li class="svc-support">Business Support</li>
    </ul>

    <div class="logo-box">
      <span class="logo-name">MCNH</span>
    </div>
  </div>
</body>
</html>
```